Web Page (Web 2.0) Re-design

We require the attached web page to be modernised. At present it looks like it was designed in the year 2000. We want the screen re-designed so that it can be considered web 2.0 at the very least, and the elements on the screen conform to web 2.0 standards, such as...
- "wow" factor on first display needed
- needs a better use of the color palette (the colours shown are what need to be used)
- font - chosen font currently boring, appropriate size changes need to be considered for emphasis where necessary
- The framed content area needs to take up a more substantial part of the screen or ALL of it if its a better output.
- rounded corners
- big and bold
- all buttons are noticeable.
- confident but smooth sectioning off of content
Please note: All the elements on the screen must be present in your design, and the placement of the screen elements in relation to each other must stay the same, but things can be bigger, bolder, smaller, funkier, wider etc. etc.
This piece of work could lead to much more work for noticeable candidates
Always happy to field questions.
19 - 40
Work

```html
<!DOCTYPE html>
<html lang="en">
<head>
<meta charset="utf-8">
<title>Blaze Hockey</title>
<link href="https://fonts.googleapis.com/css2?family=Arimo:wght@400;700&family=Oswald:wght@500;600;700&display=swap" rel="stylesheet">
<style>
:root{
  --bg:#1b1b1b;
  --panel:#1f1f1f;
  --panel-line:#3a3a3a;
  --row:#141414;
  --row-line:#2e2e2e;
  --yellow:#f5c400;
  --orange:#f29a00;
  --brand:#e8551a;
  --text:#d8d8d8;
  --muted:#8a8a8a;
  --dim:#666;
  --white:#fff;
}
*{box-sizing:border-box;margin:0;padding:0}
html,body{width:897px;height:1200px;overflow:hidden}
body{position:relative;background:radial-gradient(ellipse at 50% 35%,#3a3a3a 0%,#222 45%,var(--bg) 80%);font-family:Arimo,Arial,sans-serif;color:var(--text);font-size:10px}
.abs{position:absolute}
.header{left:0;top:0;width:897px;height:86px;background:linear-gradient(#0c0c0c,#161616);border-bottom:1px solid #2c2c2c}
.header-curve{left:0;top:40px;width:897px;height:60px}
.brand{left:122px;top:28px;display:flex;align-items:center;gap:8px}
.brand-dot{width:14px;height:14px;border-radius:50%;background:var(--brand)}
.brand-name{font-family:Oswald,sans-serif;font-weight:700;font-size:24px;letter-spacing:1px;color:var(--brand);line-height:1}
.social-mini{top:41px;width:12px;height:12px;border-radius:2px}
.search{left:580px;top:30px;width:162px;height:25px;border-radius:13px;background:linear-gradient(#2a2a2a,#1a1a1a);border:1px solid #444;color:#999;font-size:8px;padding:7px 11px}
.search svg{position:absolute;right:10px;top:6px}
.logged{left:638px;top:82px;font-family:Oswald,sans-serif;font-weight:700;font-size:16px;line-height:16px;color:var(--white);letter-spacing:1px}
.nav{left:110px;top:98px;width:677px;height:25px;border-radius:5px;background:linear-gradient(#e6e6e6,#b5b5b5);border:1px solid #777;display:flex;align-items:center;padding-left:13px;gap:9px;font-size:9.5px;color:#2a2a2a;text-transform:uppercase}
.user-select{left:633px;top:101px;width:148px;height:19px;border-radius:4px;background:linear-gradient(#555,#333);border:1px solid #222;color:#eee;font-size:8.5px;padding:4px 12px}
.user-select svg{position:absolute;right:6px;top:6px}
.tab{height:30px;background:linear-gradient(#3c3c3c,#161616);clip-path:polygon(0 0,calc(100% - 22px) 0,100% 100%,0 100%);font-family:Oswald,sans-serif;font-weight:600;font-size:14px;line-height:18px;color:var(--yellow);padding:4px 8px;letter-spacing:.3px;border-radius:4px 0 0 0}
.panel{background:var(--panel);border:1px solid var(--panel-line);border-radius:3px}
.photo{border-radius:2px}
.row{height:20px;border-radius:6px;background:var(--row);border:1px solid var(--row-line);display:flex;align-items:center;font-size:9px;color:#ccc}
.dim{color:var(--dim)}
.hours{left:606px;width:172px;height:18px;border-radius:5px;background:#141414;border:1px solid #333;font-size:7.5px;color:#999;display:flex;align-items:center;padding-left:9px}
.hours .t{position:absolute;left:67px}
.clock{position:absolute;right:1px;top:1px;width:15px;height:15px;border-radius:50%;background:radial-gradient(#ffd84a,#c28a00);border:1px solid #6b5000}
.gold-btn{width:16px;height:13px;border-radius:3px;background:linear-gradient(#ffd23a,#d89a00)}
.pill-btn{border-radius:14px;background:linear-gradient(#fff,#bdbdbd);border:1px solid #888;color:#333;font-weight:700;display:flex;align-items:center;justify-content:center;letter-spacing:.5px}
.team-card{top:459px;width:66px;height:80px;border:1px solid #555;background:#2a2a2a}
.team-card .pic{height:64px;background:linear-gradient(#d9dde2,#8b949e)}
.team-card .nm{font-size:6.5px;color:#aaa;padding:3px 4px}
.round-arrow{width:16px;height:26px;border-radius:8px;background:#111;border:1px solid #444}
.event{left:117px;font-size:9px;color:#bbb}
.gallery-pic{width:96px;height:60px;border:2px solid #ddd;background:linear-gradient(160deg,#f2f5f8 0%,#b8c7d8 55%,#6d7f99 100%)}
.follow-btn{left:630px;width:148px;height:41px;border-radius:4px;background:linear-gradient(#3e4450,#1a1d22);border:1px solid #4a4f58;display:flex;align-items:center;padding-left:6px;gap:8px}
.follow-btn .ico{width:30px;height:30px;border-radius:4px}
.follow-btn b{display:block;font-size:11px;color:#9fc4e8}
.follow-btn span{font-size:8px;color:#ddd}
.footer{top:1164px;left:118px;font-size:9px;color:#999}
.copyright{top:1164px;left:586px;width:200px;text-align:right;font-size:9px;color:#999}
</style>
</head>
<body>

<header class="abs header">
  <svg class="abs header-curve" viewBox="0 0 897 60" width="897" height="60"><path d="M0 50 Q450 0 897 25" fill="none" stroke="#3a3a3a" stroke-width="1.5"/></svg>
</header>
<div class="abs brand"><span class="brand-dot"></span><span class="brand-name">BLAZE HOCKEY</span></div>
<span class="abs social-mini" style="left:530px;background:#5aa8d6"></span>
<span class="abs social-mini" style="left:545px;background:#3b5a9a"></span>
<span class="abs social-mini" style="left:561px;background:#c8302a"></span>
<div class="abs search">Search...
  <svg width="12" height="12" viewBox="0 0 12 12"><circle cx="5" cy="5" r="3.6" fill="none" stroke="#ddd" stroke-width="1.6"/><path d="M7.6 7.6 11 11" stroke="#ddd" stroke-width="1.8"/></svg>
</div>

<nav class="abs nav"><span>Home</span><span>What is Blaze Hockey?</span><span>Where to play</span><span>The rules</span><span>Challenge your friends</span><span>Contact</span></nav>
<div class="abs logged">LOGGED THE</div>
<div class="abs user-select">Dale Preston
  <svg width="8" height="5" viewBox="0 0 8 5"><path d="M0 0h8L4 5z" fill="#ddd"/></svg>
</div>

<!-- Red Room -->
<div class="abs tab" style="left:110px;top:137px;width:96px">RED ROOM</div>
<section class="abs panel" style="left:110px;top:166px;width:336px;height:241px"></section>
<div class="abs photo" role="img" aria-label="Players contesting the ball in a field hockey match" style="left:115px;top:171px;width:327px;height:176px;background:linear-gradient(160deg,#6f8fa8 0%,#c9c27a 40%,#3f7a4f 100%)"></div>
<div class="abs" style="left:115px;top:306px;width:327px;height:41px;background:rgba(0,0,0,.6);padding:4px 3px">
  <div style="font-weight:700;font-size:9px;color:#fff">Next generation of Green Gliders look to impress</div>
  <div style="font-size:8px;color:#ddd;margin-top:2px;line-height:12px">While the Green Gliders are working hard to prepare for the 2012 Summer Cup, the next crop of...</div>
</div>
<svg class="abs" style="left:117px;top:367px" width="12" height="20" viewBox="0 0 12 20"><path d="M10 2 2 10l8 8" fill="none" stroke="#fff" stroke-width="3"/></svg>
<svg class="abs" style="left:429px;top:367px" width="12" height="20" viewBox="0 0 12 20"><path d="M2 2l8 8-8 8" fill="none" stroke="#fff" stroke-width="3"/></svg>
<div class="abs photo" role="img" aria-label="Match thumbnail" style="left:133px;top:354px;width:67px;height:45px;border:1px solid #ccc;background:linear-gradient(#6f9fc0,#3d7a50)"></div>
<div class="abs photo" role="img" aria-label="Match thumbnail" style="left:208px;top:354px;width:67px;height:45px;border:1px solid #ccc;background:linear-gradient(#7c6a3a,#c2a23a)"></div>
<div class="abs photo" role="img" aria-label="Match thumbnail" style="left:283px;top:354px;width:67px;height:45px;border:1px solid #ccc;background:linear-gradient(#4aa58e,#2f7a68)"></div>
<div class="abs photo" role="img" aria-label="Team huddle thumbnail" style="left:358px;top:354px;width:67px;height:45px;border:1px solid #ccc;background:linear-gradient(#7fb0d8,#c9a82a)"></div>

<!-- Venue Profile -->
<div class="abs tab" style="left:452px;top:137px;width:128px">VENUE PROFILE</div>
<section class="abs panel" style="left:452px;top:166px;width:334px;height:185px"></section>
<div class="abs" role="img" aria-label="Street map of the venue location" style="left:460px;top:175px;width:138px;height:77px;border:2px solid #ccc;background:linear-gradient(135deg,#d6dbc4,#b9c7a4)"></div>
<div class="abs" style="left:460px;top:257px;font-size:11px;color:#fff">Lorem ipsum</div>
<div class="abs" style="left:460px;top:272px;font-size:8.5px;color:#bbb;line-height:12.3px">Lorem ipsum dolor, sit amet<br>P: 555-210-8574 (7825)<br>F:&nbsp;&nbsp; 555-210-1254<br>E:&nbsp; info@rinkhall.net<br><span style="display:inline-block;margin-top:3px">www.rinkhall.net</span></div>
<span class="abs social-mini" style="left:554px;top:321px;background:#5aa8d6"></span>
<span class="abs social-mini" style="left:569px;top:321px;background:#3b5a9a"></span>
<div class="abs" style="left:608px;top:173px;font-size:12px;color:#eee">OPENING HOURS</div>
<div class="abs hours" style="top:193px">Monday<span class="t">6:00am - 11:00pm</span><i class="clock"></i></div>
<div class="abs hours" style="top:215px">Tuesday<span class="t">6:00am - 11:00pm</span><i class="clock"></i></div>
<div class="abs hours" style="top:237px">Wednesday<span class="t">6:00am - 11:00pm</span><i class="clock"></i></div>
<div class="abs hours" style="top:260px">Thursday<span class="t">6:00am - 11:00pm</span><i class="clock"></i></div>
<div class="abs hours" style="top:282px">Friday<span class="t">6:00am - 11:00pm</span><i class="clock"></i></div>
<div class="abs hours" style="top:304px">Saturday<span class="t">6:00am - 11:00pm</span><i class="clock"></i></div>
<div class="abs hours" style="top:326px">Sunday<span class="t">6:00am - 11:00pm</span><i class="clock"></i></div>

<!-- My Teams -->
<div class="abs tab" style="left:452px;top:367px;width:92px">MY TEAMS</div>
<section class="abs panel" style="left:452px;top:396px;width:334px;height:177px"></section>
<div class="abs" style="left:472px;top:417px;font-size:8.5px;color:#ccc">Dropdown List</div>
<div class="abs" style="left:541px;top:410px;width:138px;height:23px;border-radius:4px;background:linear-gradient(#f4f4f4,#c9c9c9);font-size:9px;color:#333;padding:6px 7px">Select an option...
  <span style="position:absolute;right:0;top:0;width:24px;height:21px;border-left:1px solid #999"></span>
  <svg style="position:absolute;right:8px;top:8px" width="8" height="5" viewBox="0 0 8 5"><path d="M0 0h8L4 5z" fill="#444"/></svg>
</div>
<div class="abs" style="left:472px;top:439px;font-size:12px;color:#eee">CREATE NEW TEAM</div>
<div class="abs round-arrow" style="left:450px;top:482px"><svg width="16" height="26" viewBox="0 0 16 26"><path d="M9 9 5 13l4 4" fill="none" stroke="#ccc" stroke-width="2"/></svg></div>
<div class="abs round-arrow" style="left:773px;top:482px"><svg width="16" height="26" viewBox="0 0 16 26"><path d="M7 9l4 4-4 4" fill="none" stroke="#ccc" stroke-width="2"/></svg></div>
<div class="abs team-card" style="left:473px"><div class="pic" role="img" aria-label="Player photo"></div><div class="nm">Name</div></div>
<div class="abs team-card" style="left:546px"><div class="pic" role="img" aria-label="Player photo"></div><div class="nm">Name</div></div>
<div class="abs team-card" style="left:619px"><div class="pic" role="img" aria-label="Player photo"></div><div class="nm">Name</div></div>
<div class="abs team-card" style="left:691px"><div class="pic" role="img" aria-label="Player photo"></div><div class="nm">Name</div></div>
<svg class="abs" style="left:473px;top:544px" width="14" height="14" viewBox="0 0 14 14"><path d="M2 7l3.5 4L12 2" fill="none" stroke="var(--yellow)" stroke-width="2.6"/></svg>
<div class="abs" style="left:494px;top:547px;font-size:9px;color:#bbb">Soolding New Players</div>
<div class="abs" style="left:588px;top:543px;width:16px;height:16px;border-radius:50%;background:radial-gradient(#ffd84a,#c28a00)"><svg width="16" height="16" viewBox="0 0 16 16"><path d="M8 4v8M4 8h8" stroke="#3a2a00" stroke-width="2"/></svg></div>
<div class="abs" style="left:612px;top:547px;font-size:9px;color:#bbb">Edit Team</div>
<div class="abs" style="left:663px;top:543px;width:16px;height:16px;border-radius:50%;background:radial-gradient(#ffd84a,#c28a00)"><svg width="16" height="16" viewBox="0 0 16 16"><circle cx="8" cy="6" r="2.4" fill="#3a2a00"/><path d="M4 12.5c.6-2.6 7.4-2.6 8 0z" fill="#3a2a00"/></svg></div>
<div class="abs" style="left:686px;top:547px;font-size:9px;color:#bbb">Invite Friends</div>

<!-- Next Competition -->
<div class="abs tab" style="left:110px;top:422px;width:142px">NEXT COPETITION</div>
<section class="abs panel" style="left:110px;top:451px;width:336px;height:122px"></section>
<div class="abs row" style="left:116px;top:457px;width:324px;padding-left:9px">21st July, 2011<span style="position:absolute;left:89px">Team A&nbsp; Vs&nbsp; Team B</span></div>
<div class="abs row" style="left:116px;top:479px;width:324px;padding-left:9px">25st July, 2011<span style="position:absolute;left:89px">Team A&nbsp; Vs&nbsp; Team B</span></div>
<div class="abs row" style="left:116px;top:501px;width:324px;padding-left:9px">28st July, 2011<span style="position:absolute;left:89px">Team A&nbsp; Vs&nbsp; Team B</span></div>
<div class="abs row" style="left:116px;top:522px;width:324px;padding-left:9px">30st July, 2011<span style="position:absolute;left:89px">Team A&nbsp; Vs&nbsp; Team B</span></div>
<div class="abs row" style="left:116px;top:544px;width:324px;padding-left:9px">30st July, 2011<span style="position:absolute;left:89px">Team A&nbsp; Vs&nbsp; Team B</span></div>

<!-- My Competitions -->
<div class="abs tab" style="left:110px;top:587px;width:145px">MY COMPETITIONS</div>
<section class="abs panel" style="left:110px;top:616px;width:336px;height:209px"></section>
<div class="abs" style="left:120px;top:626px;font-size:8.5px;color:#fff;font-weight:700">All</div>
<div class="abs" style="left:144px;top:626px;font-size:8.5px;color:#fff;font-weight:700">Entered But Not Scored</div>
<div class="abs" style="left:260px;top:626px;font-size:8.5px;color:#fff;font-weight:700">In Progress</div>
<div class="abs" style="left:369px;top:626px;font-size:8.5px;color:#fff;font-weight:700">Completed</div>
<div class="abs row" style="left:118px;top:644px;width:322px;padding-left:7px">Monday Night leagues<span class="dim" style="position:absolute;left:142px">Lorem ipsum dolor</span><span class="dim" style="position:absolute;left:251px">Scored</span><i class="abs gold-btn" style="left:304px;top:3px"></i></div>
<div class="abs row" style="left:118px;top:666px;width:322px;padding-left:7px">Monday Night leagues<span class="dim" style="position:absolute;left:142px">Lorem ipsum dolor</span><span class="dim" style="position:absolute;left:251px">In progress</span></div>
<div class="abs row" style="left:118px;top:688px;width:322px;padding-left:7px">Monday Night leagues<span class="dim" style="position:absolute;left:142px">Lorem ipsum dolor</span><span class="dim" style="position:absolute;left:251px">Completed</span></div>
<div class="abs row" style="left:118px;top:709px;width:322px;padding-left:7px">Monday Night leagues<span class="dim" style="position:absolute;left:142px">Lorem ipsum dolor</span><span class="dim" style="position:absolute;left:251px">Scored</span><i class="abs gold-btn" style="left:304px;top:3px"></i></div>
<div class="abs row" style="left:118px;top:731px;width:322px;padding-left:7px">Monday Night leagues<span class="dim" style="position:absolute;left:142px">Lorem ipsum dolor</span><span class="dim" style="position:absolute;left:251px">In progress</span></div>
<div class="abs row" style="left:118px;top:752px;width:322px;padding-left:7px">Saturdayday Night leagues<span class="dim" style="position:absolute;left:142px">Lorem ipsum dolor</span><span class="dim" style="position:absolute;left:251px">Completed</span></div>
<div class="abs row" style="left:118px;top:774px;width:322px;padding-left:7px">Monday Night leagues<span class="dim" style="position:absolute;left:142px">Lorem ipsum dolor</span><span class="dim" style="position:absolute;left:251px">Scored</span><i class="abs gold-btn" style="left:304px;top:3px"></i></div>
<div class="abs row" style="left:118px;top:796px;width:322px;padding-left:7px">Monday Night leagues<span class="dim" style="position:absolute;left:142px">Lorem ipsum dolor</span><span class="dim" style="position:absolute;left:251px">Completed</span></div>

<!-- Operating Leagues -->
<div class="abs tab" style="left:452px;top:587px;width:160px">OPERATING LEAGUES</div>
<section class="abs panel" style="left:452px;top:616px;width:334px;height:209px"></section>
<div class="abs" style="left:459px;top:624px;width:320px;height:24px;border-radius:4px;background:#151515;border:1px solid #333;text-align:center;font-size:9px;color:#fff;padding-top:7px">League 2010-11</div>
<div class="abs" style="left:460px;top:625px;width:24px;height:22px;border-radius:3px;background:linear-gradient(#ffd23a,#c98e00)"><svg width="24" height="22" viewBox="0 0 24 22"><path d="M16 8h-6V5l-5 6 5 6v-3h6z" fill="#fff"/></svg></div>
<div class="abs" style="left:754px;top:625px;width:24px;height:22px;border-radius:3px;background:linear-gradient(#ffd23a,#c98e00)"><svg width="24" height="22" viewBox="0 0 24 22"><path d="M8 8h6V5l5 6-5 6v-3H8z" fill="#fff"/></svg></div>
<div class="abs" style="left:452px;top:661px;width:334px;text-align:center">
  <div style="font-size:12px;color:#fff">THURSDAY NIGHT LEAGUE</div>
  <div style="font-size:8.5px;color:#bbb;line-height:11.7px;margin-top:3px">Prairie Storm<br>212 N. Elm<br>Suite 100<br>Harlow, KS 67219<br>(555) 301-4410 (ph)<br>(555) 301-4411 (f)<br>www.prairiestorm.com</div>
  <div style="font-size:8.5px;color:var(--orange);margin-top:8px">View Leagues Table</div>
</div>
<div class="abs pill-btn" style="left:552px;top:787px;width:136px;height:24px;font-size:12px">ENTER LEAGUES</div>

<!-- Upcoming Events -->
<div class="abs" style="left:110px;top:835px;font-family:Oswald,sans-serif;font-weight:600;font-size:14px;line-height:18px;color:var(--yellow)">UPCOMING EVENTS</div>
<section class="abs" style="left:110px;top:860px;width:336px;height:81px;border:1px solid #333;background:#1c1c1c"></section>
<div class="abs event" style="top:868px">National Men's Hockey League - 6-13 August: Sydney, NSW</div>
<div class="abs event" style="top:889px">National U15 Indoor Championship, Boys &amp; Girls, 3 - 8 Jan: Wollongong, NSW</div>
<div class="abs event" style="top:910px">National Men's Hockey League - 6-13 August: Sydney, NSW</div>
<div class="abs" style="left:351px;top:927px;font-size:6.5px;color:var(--orange)">MORE UPCOMING EVENTS</div>

<!-- Photo Gallery -->
<div class="abs tab" style="left:110px;top:955px;width:132px">PHOTO GALLERY</div>
<section class="abs panel" style="left:110px;top:984px;width:336px;height:162px"></section>
<div class="abs" style="left:392px;top:962px;width:47px;height:13px;border-radius:2px;background:linear-gradient(#c52a1a,#7a1208);font-size:6.5px;color:#fff;text-align:center;padding-top:3px">VIEW ALLL</div>
<div class="abs gallery-pic" role="img" aria-label="Ice hockey game action" style="left:125px;top:999px"></div>
<div class="abs gallery-pic" role="img" aria-label="Ice hockey game action" style="left:231px;top:999px"></div>
<div class="abs gallery-pic" role="img" aria-label="Ice hockey game action" style="left:337px;top:999px"></div>
<div class="abs gallery-pic" role="img" aria-label="Ice hockey game action" style="left:125px;top:1071px"></div>
<div class="abs gallery-pic" role="img" aria-label="Ice hockey game action" style="left:231px;top:1071px"></div>
<div class="abs gallery-pic" role="img" aria-label="Ice hockey game action" style="left:337px;top:1071px"></div>

<!-- Enter Results -->
<div class="abs tab" style="left:452px;top:840px;width:128px">ENTER RESULTS</div>
<section class="abs panel" style="left:452px;top:869px;width:164px;height:167px"></section>
<div class="abs" style="left:459px;top:881px;font-size:8.5px;color:#fff">Matches Requiring Conformation</div>
<div class="abs" style="left:458px;top:902px;width:152px;height:131px;border-radius:5px;background:linear-gradient(#d2d2d2,#9d9d9d);border:1px solid #777"></div>
<div class="abs" style="left:458px;top:902px;width:152px;height:21px;border-radius:5px 5px 0 0;background:linear-gradient(#6e6e6e,#3c3c3c);font-size:11px;color:#fff;text-align:center;padding-top:4px">Monday Night League</div>
<div class="abs" style="left:466px;top:933px;width:137px;height:18px;border-radius:3px;background:#1a1a1a;border:1px solid #555;font-size:9px;color:#fff;font-weight:700;padding:4px 6px">JUL<span style="position:absolute;left:57px;font-weight:400">25th</span><span style="position:absolute;left:108px;font-weight:400">3pm</span></div>
<div class="abs" style="left:483px;top:956px;font-size:9px;color:#222">Team A</div>
<div class="abs" style="left:554px;top:956px;font-size:9px;color:#222">Team B</div>
<div class="abs" style="left:472px;top:972px;width:57px;height:26px;border-radius:5px;background:linear-gradient(#fff,#d6d6d6);border:1px solid #888;font-size:13px;font-weight:700;color:#222;text-align:center;padding-top:5px">000</div>
<div class="abs" style="left:543px;top:972px;width:57px;height:26px;border-radius:5px;background:linear-gradient(#fff,#d6d6d6);border:1px solid #888;font-size:13px;font-weight:700;color:#222;text-align:center;padding-top:5px">000</div>
<div class="abs pill-btn" style="left:466px;top:1006px;width:136px;height:22px;font-size:12px">CONFIRM SCORE</div>

<!-- Follow Us -->
<div class="abs tab" style="left:622px;top:840px;width:128px">FOLLOW US</div>
<section class="abs panel" style="left:622px;top:869px;width:164px;height:167px"></section>
<div class="abs follow-btn" style="top:877px"><i class="ico" style="background:#3b5a9a"></i><div><b>Friendbook</b><span>Join our group</span></div></div>
<div class="abs follow-btn" style="top:926px"><i class="ico" style="background:#5aa8d6"></i><div><b>Chirper</b><span>Follow Us</span></div></div>
<div class="abs follow-btn" style="top:975px"><i class="ico" style="background:#c8302a"></i><div><b>ViewTube</b><span>Watch Us On ViewTube</span></div></div>

<!-- Newsletter -->
<section class="abs" role="img" aria-label="Newsletter banner with a hockey player in motion" style="left:452px;top:1050px;width:334px;height:86px;border-radius:6px;background:linear-gradient(100deg,#e2a21e 0%,#b0281c 35%,#6a1410 100%)"></section>
<div class="abs" style="left:460px;top:1068px;font-family:Oswald,sans-serif;font-weight:700;font-size:18px;line-height:22px;color:var(--yellow);letter-spacing:2px">NEWSLETTER SIGN UP</div>
<div class="abs" style="left:497px;top:1105px;font-size:8.5px;color:#fff">For Newsletters &amp; Updates Join Our Mailing List</div>
<div class="abs" style="left:497px;top:1128px;width:183px;height:18px;background:linear-gradient(#fff,#ddd);font-size:8.5px;color:#333;padding:4px 7px">Enter Your Email...</div>
<div class="abs" style="left:678px;top:1128px;width:55px;height:18px;border-radius:2px;background:linear-gradient(#ffd23a,#e0a000);font-size:11px;font-weight:700;color:#3a2400;text-align:center;padding-top:2px">Submit</div>

<!-- Footer -->
<footer class="abs footer">HOME&nbsp; |&nbsp; WHAT IS BLAZE HOCKEY?&nbsp; |&nbsp; WHERE TO PLAY&nbsp; |&nbsp; THE RULES&nbsp; |&nbsp; CHALLENGE YOUR FRIENDS&nbsp; |&nbsp; CONTACT</footer>
<div class="abs copyright">COPYRIGHT 2011 BLAZE HOCKEY</div>

</body>
</html>
```